Marrowgate Auctions Business Cards Design Needed

I need a business card design that is modern looking - double sided (maybe just my logo on the back, but open to suggestions) - the overall design is up to you. I want it to be easy to read - not over the top flashy. I already have a company logo which I uploaded so that needs to be used. The colors of my logo are the colors I want on the card... so blue and gray (do need to match the logo colors).

Requirements
Must have
• Would like the card to be sleek, modern and easy to ready

```html
<!DOCTYPE html>
<html lang="en">
<head>
<meta charset="utf-8">
<title>Marrowgate Auctions – Business Card</title>
<link rel="stylesheet" href="https://fonts.googleapis.com/css2?family=Open+Sans:wght@400;600;700&display=swap">
<style>
  :root {
    --backdrop: #2b2b2d;
    --brand-blue: #2f78b7;
    --brand-blue-dark: #23619a;
    --brand-gray: #4a4a4c;
    --card-white: #f4f4f4;
    --text-dark: #333335;
    --rule: #3a3a3a;
  }
  * { margin: 0; padding: 0; box-sizing: border-box; }
  html, body {
    width: 1200px; height: 997px; overflow: hidden;
    background: var(--backdrop);
    font-family: "Open Sans", Arial, sans-serif;
  }
  .sheet {
    position: relative; width: 1200px; height: 997px;
  }
  .card {
    position: absolute; left: 220px; width: 760px; height: 434px;
    overflow: hidden;
  }
  /* Back of card */
  .card--back {
    top: 48px;
    background: var(--brand-blue);
    display: flex; align-items: center; justify-content: center;
  }
  .card--back .brand-name {
    color: #ffffff; font-weight: 700; font-size: 72px; letter-spacing: 1px;
  }
  /* Front of card */
  .card--front {
    top: 515px;
    background: linear-gradient(160deg, #ffffff 0%, var(--card-white) 60%, #e9e9e9 100%);
  }
  .front-logo {
    position: absolute; top: 70px; left: 0; width: 100%;
    text-align: center;
    color: var(--brand-blue); font-weight: 700; font-size: 44px; letter-spacing: 1px;
  }
  .front-rule {
    position: absolute; top: 175px; left: 260px; width: 460px; height: 1px;
    background: var(--rule);
  }
  .holder {
    position: absolute; top: 162px; left: 48px;
  }
  .holder__name {
    color: var(--brand-blue); font-weight: 700; font-size: 20px; letter-spacing: 0.5px;
  }
  .holder__title {
    color: var(--text-dark); font-size: 17px; margin-top: 2px;
  }
  .address {
    position: absolute; top: 130px; right: 40px; text-align: right;
    color: var(--brand-blue); font-size: 15px; line-height: 1.35;
  }
  .contacts {
    position: absolute; top: 258px; left: 48px; list-style: none;
  }
  .contacts li {
    display: flex; align-items: center; gap: 12px;
    color: var(--text-dark); font-size: 17px; height: 28px;
  }
  .contacts svg { width: 18px; height: 18px; flex: none; }
  .bands {
    position: absolute; left: 0; bottom: 0; width: 760px; height: 160px;
  }
  .web {
    position: absolute; right: 36px; top: 312px;
    color: #ffffff; font-weight: 700; font-size: 18px;
  }
</style>
</head>
<body>
<main class="sheet">

  <section class="card card--back" aria-label="Card back">
    <span class="brand-name">MARROWGATE</span>
  </section>

  <section class="card card--front" aria-label="Card front">
    <div class="front-logo">MARROWGATE AUCTIONS</div>
    <div class="front-rule"></div>

    <div class="holder">
      <div class="holder__name">ELENA VARKOVA</div>
      <div class="holder__title">Director</div>
    </div>

    <div class="address">
      Suite 4.12 88 Harbour Lane<br>NSW 2015
    </div>

    <svg class="bands" viewBox="0 0 760 160" aria-hidden="true">
      <path d="M430 0 H760 V160 H0 V150 H360 C400 150 400 40 430 0 Z" fill="var(--brand-blue)"/>
      <path d="M0 118 H380 C392 118 396 110 400 100 L404 100 C400 120 392 128 380 128 H0 Z" fill="var(--brand-gray)"/>
      <path d="M0 128 H380 C394 128 402 118 406 104 L760 104 V112 L414 112 C408 132 398 140 380 140 H0 Z" fill="#ffffff"/>
      <rect x="0" y="140" width="760" height="20" fill="var(--brand-blue-dark)"/>
    </svg>
    <div class="web">www.marrowgateauctions.com.au</div>

    <ul class="contacts">
      <li>
        <svg viewBox="0 0 20 20" aria-hidden="true"><circle cx="10" cy="10" r="10" fill="var(--brand-blue)"/><path d="M6 7.5c0-1 1-1.5 4-1.5s4 .5 4 1.5v1h-2v-1h-4v1H6z M7 9h6l1 5H6z" fill="#fff"/></svg>
        <span>02 91004820</span>
      </li>
      <li>
        <svg viewBox="0 0 20 20" aria-hidden="true"><circle cx="10" cy="10" r="10" fill="var(--brand-blue)"/><rect x="7" y="4.5" width="6" height="11" rx="1" fill="#fff"/><rect x="8" y="6" width="4" height="7" fill="var(--brand-blue)"/></svg>
        <span>0412 555 730</span>
      </li>
      <li>
        <svg viewBox="0 0 20 20" aria-hidden="true"><circle cx="10" cy="10" r="10" fill="var(--brand-blue)"/><rect x="5" y="6.5" width="10" height="7" fill="#fff"/><path d="M5 6.5l5 4 5-4" fill="none" stroke="var(--brand-blue)" stroke-width="1"/></svg>
        <span>elena@marrowgateauctions.com.au</span>
      </li>
    </ul>
  </section>

</main>
</body>
</html>
```